Goal Planning Work Sheet

Design a better Goal Planning Worksheet that is fillable

Target Market(s)

People looking to make an important change

Industry/Entity Type

Work

Requirements
Must have
• Fillable pdf form
• Exceptional Design

```html
<!DOCTYPE html>
<html lang="en">
<head>
<meta charset="utf-8">
<title>Steady Steps Ahead – Goal Planning Worksheet</title>
<link rel="stylesheet" href="https://fonts.googleapis.com/css2?family=Open+Sans:wght@400;700&display=swap">
<style>
  :root {
    --sidebar: #a9dce8;
    --fade: #b8e2ec;
    --teal: #1a8fa3;
    --navy: #1c4a86;
    --ink: #2a4a5a;
    --disc: #d6eef4;
    --paper: #ffffff;
  }
  * { box-sizing: border-box; margin: 0; padding: 0; }
  html, body { width: 1200px; height: 800px; overflow: hidden; }
  body { font-family: "Open Sans", Arial, sans-serif; background: var(--paper); }
  .sheet {
    position: relative; width: 1200px; height: 800px;
    display: grid; grid-template-columns: 250px 1fr;
    background: linear-gradient(90deg, var(--paper) 0%, var(--paper) 72%, var(--fade) 100%);
  }
  .sidebar { background: var(--sidebar); padding: 22px 18px 20px 30px; color: var(--ink); }
  .brand { display: flex; flex-direction: column; align-items: center; gap: 12px; margin-bottom: 18px; }
  .brand-name {
    font-weight: 700; color: var(--navy); font-size: 22px; line-height: 1.2;
    text-align: center;
  }
  .brand-mark { display: block; }
  .side-heading { font-weight: 700; color: var(--navy); font-size: 13px; margin-top: 14px; }
  .side-list { list-style: none; font-size: 10.5px; line-height: 1.3; margin-top: 3px; }
  .side-list li { position: relative; padding-left: 12px; margin-bottom: 1px; }
  .side-list li::before {
    content: ""; position: absolute; left: 2px; top: 6px;
    width: 4px; height: 4px; border-radius: 50%; background: var(--teal);
  }
  .side-list b { color: var(--navy); }
  .worksheet { position: relative; }
  .field { position: absolute; left: 18px; }
  .field-label {
    display: inline-block; background: var(--teal); color: #fff;
    font-weight: 700; font-size: 12.5px; padding: 4px 10px; letter-spacing: .2px;
  }
  .f-imagine { top: 22px; }
  .f-specific { top: 140px; }
  .f-roadblocks { top: 420px; }
  .f-team { top: 580px; }
  .f-evaluate { top: 690px; }
</style>
</head>
<body>
<main class="sheet">
  <aside class="sidebar">
    <div class="brand">
      <h1 class="brand-name">Steady Steps Ahead</h1>
      <svg class="brand-mark" width="90" height="90" viewBox="0 0 90 90" aria-hidden="true">
        <circle cx="45" cy="45" r="45" fill="var(--disc)"/>
      </svg>
    </div>

    <h2 class="side-heading">Strength Spotting</h2>
    <ul class="side-list">
      <li><b>Wisdom:</b> Cognitive Creativity Curiosity Judgment Love of Learning Perspective</li>
      <li><b>Courage:</b> Bravery Perseverance Honesty Zest</li>
      <li><b>Humanity:</b> Love Kindness Social Intelligence Teamwork</li>
      <li><b>Justice:</b> Fairness Leadership</li>
      <li><b>Temperance:</b> Forgiveness Humility Prudence Self Regulation</li>
      <li><b>Transcendence:</b> Appreciation Beauty &amp; Excellence Gratitude Hope Humor Spirituality</li>
    </ul>

    <h2 class="side-heading">DARE</h2>
    <ul class="side-list">
      <li>Fuse To Thoughts and Feelings</li>
      <li>Excessive Thinking</li>
      <li>Attraction: Negative Emotional</li>
      <li>Run Away &amp; Avoidance</li>
    </ul>

    <h2 class="side-heading">FEAR</h2>
    <ul class="side-list">
      <li><b>Defuse:</b> Notice, Name, Normalize</li>
      <li><b>Acceptance:</b> Allow, Appreciate Reinforce Skills &amp; Support Enjoy Values</li>
    </ul>

    <h2 class="side-heading">Problem Solving Process</h2>
    <ul class="side-list">
      <li>Domain of Problem</li>
      <li>Team Gathered</li>
      <li>Values Focus</li>
      <li>Imagine, Move, Be</li>
      <li>Define Problem, Cause, Solutions</li>
      <li>Plan-SMARTER Goals</li>
      <li>Resources &amp; Resourcefulness</li>
      <li>Practice, Rehearse</li>
      <li>Act Communicate</li>
      <li>Evaluate Revise</li>
    </ul>
  </aside>

  <section class="worksheet">
    <div class="field f-imagine"><span class="field-label">Imagine and Move (motion creates emotion) Being the person I want to be, Values, Character Strengths:</span></div>
    <div class="field f-specific"><span class="field-label">Specific Small Meaningful Measurable Actionable Attainable Timeline Now:</span></div>
    <div class="field f-roadblocks"><span class="field-label">Roadblocks Resources Rewards Ramification:</span></div>
    <div class="field f-team"><span class="field-label">Team Roles:</span></div>
    <div class="field f-evaluate"><span class="field-label">Evaluate, Emotions, Revise, Resilient</span></div>
  </section>
</main>
</body>
</html>
```